User Interface Design for new Team Management App

We're developing a new app with a unique, two part, user interface. The artistic section of our UI is complete, we now need the functional part completed. The functional part will include menus, inputting data, scrolling and etc. We have our own developers and coders, so no need to worry about that.

The contest:
The artist we decide to work with will submit a design which will be their vision for the entirety of the project. See the brief for more information, it is attached.

Points to remember:
-We like artists to submit fast
-Please follow the brief
-Please show examples of other UI work you have completed in the past
-We like people who communicate promptly, openly and professionally.

Thank you, and good luck.

Industry/Entity Type

Management

```html
<!DOCTYPE html>
<html lang="en">
<head>
<meta charset="utf-8">
<title>Team Deck – Onboarding Screens</title>
<link rel="stylesheet" href="https://fonts.googleapis.com/css2?family=Lato:ital,wght@0,400;1,400&family=Inter:wght@400&display=swap">
<style>
  :root {
    --stage-bg: #333333;
    --stage-shadow: #3d3d3d;
    --title-ink: #ffffff;
    --card-bg: #ffffff;
    --ink: #1d1d1d;
    --accent: #d0605e;
    --accent-soft: #e9cfd0;
    --rule: #e3aeb0;
    --muted: #efefef;
    --close: #c8c8c8;
    --wash-violet: #8f8fc6;
    --wash-rose: #b56a8a;
    --wash-green: #7fb77a;
    --wash-blue: #6f9bc4;
    --wash-gold: #e6cf86;
  }
  * { box-sizing: border-box; margin: 0; padding: 0; }
  html, body {
    width: 1200px; height: 1000px; overflow: hidden;
    background: var(--stage-bg);
  }
  .stage {
    position: relative; width: 1200px; height: 1000px;
    background: linear-gradient(135deg, var(--stage-bg) 55%, var(--stage-shadow) 55.1%, var(--stage-bg) 85%);
  }
  .screen-title {
    position: absolute; top: 30px; width: 480px;
    font-family: "Inter", Helvetica, Arial, sans-serif;
    font-size: 40px; color: var(--title-ink); text-align: center;
  }
  .screen {
    position: absolute; top: 119px; width: 480px; height: 851px; overflow: hidden;
  }
  .screen-wash {
    position: absolute; inset: 0;
    background:
      radial-gradient(ellipse 60% 30% at 15% 20%, var(--wash-violet), transparent 70%),
      radial-gradient(ellipse 50% 20% at 85% 3%, var(--wash-rose), transparent 70%),
      radial-gradient(ellipse 30% 30% at 100% 35%, var(--wash-green), transparent 70%),
      radial-gradient(ellipse 35% 35% at 100% 70%, var(--wash-blue), transparent 70%),
      radial-gradient(ellipse 55% 35% at 10% 75%, var(--wash-gold), transparent 70%),
      radial-gradient(ellipse 50% 15% at 40% 100%, var(--wash-gold), transparent 70%),
      #e9e6e2;
  }
  .card {
    position: absolute; left: 15px; top: 14px; width: 450px; height: 742px;
    background: var(--card-bg); border-radius: 18px; overflow: hidden;
  }
  .crest-band {
    position: absolute; left: 0; top: 60px; width: 100%; height: 66px;
    background: linear-gradient(90deg, var(--accent-soft) 25%, #fff 42%, #fff 58%, var(--accent-soft) 75%);
  }
  .crest {
    position: absolute; left: 162px; top: 15px; width: 126px; height: 154px;
    border-radius: 50% 50% 40% 40%;
    background: radial-gradient(ellipse 28% 30% at 50% 42%, #3a3a40 60%, #7e9fc0 75%, #f3dcdc 82%, #fbeeee 100%);
  }
  .close {
    position: absolute; right: 14px; top: 16px; width: 28px; height: 28px;
  }
  .card-rule {
    position: absolute; left: 0; width: 100%;
  }
  .card-rule.thick { top: 704px; height: 3px; background: var(--rule); }
  .card-rule.thin { top: 711px; height: 1px; background: var(--rule); }
  .choices { position: absolute; left: 14px; top: 204px; width: 422px; list-style: none; }
  .choice {
    display: flex; gap: 14px; align-items: flex-start; margin-bottom: 29px;
    font-family: "Lato", sans-serif; font-size: 18px; line-height: 24px; color: var(--ink);
    text-align: justify;
  }
  .choice svg { flex: none; width: 40px; height: 40px; margin-top: 3px; }
  .copy {
    position: absolute; left: 15px; top: 204px; width: 420px;
    font-family: "Lato", sans-serif; font-size: 18px; line-height: 24.5px;
    color: var(--ink); text-align: justify;
  }
  .copy .quote { font-style: italic; color: var(--accent); margin-bottom: 29px; }
  .copy p + p { margin-top: 24px; }
  .next-button {
    position: absolute; left: 15px; top: 772px; width: 450px; height: 64px;
    background: var(--accent); color: #fff; border: none;
    font-family: "Lato", sans-serif; font-size: 24px; letter-spacing: 0.5px;
  }
</style>
</head>
<body>
<main class="stage">

  <h2 class="screen-title" style="left:108px">Screen 2</h2>
  <section class="screen" style="left:106px">
    <div class="screen-wash" role="img" aria-label="Soft watercolour wash background in violet, rose, green, blue and gold"></div>
    <div class="card">
      <div class="crest-band"></div>
      <div class="crest" role="img" aria-label="Ornate pink crest framing a portrait of a hooded guide"></div>
      <svg class="close" viewBox="0 0 28 28" aria-label="Close"><path d="M3 3L25 25M25 3L3 25" stroke="var(--close)" stroke-width="3.5"/></svg>
      <ul class="choices">
        <li class="choice">
          <svg viewBox="0 0 40 40"><circle cx="20" cy="20" r="19" fill="var(--accent)"/><path d="M11 20.5l6 6 12-13" fill="none" stroke="#fff" stroke-width="3"/></svg>
          <span>I am the leader of a team and I want to create a new deck to help me lead it.</span>
        </li>
        <li class="choice">
          <svg viewBox="0 0 40 40"><circle cx="20" cy="20" r="19" fill="var(--muted)"/><path d="M11 20.5l6 6 12-13" fill="none" stroke="#fff" stroke-width="3"/></svg>
          <span>I am part of a team and I want to join a deck that already exists.</span>
        </li>
      </ul>
      <div class="card-rule thick"></div>
      <div class="card-rule thin"></div>
    </div>
    <button class="next-button">NEXT</button>
  </section>

  <h2 class="screen-title" style="left:613px">Screen 3</h2>
  <section class="screen" style="left:619px">
    <div class="screen-wash" role="img" aria-label="Soft watercolour wash background in violet, rose, green, blue and gold"></div>
    <div class="card">
      <div class="crest-band"></div>
      <div class="crest" role="img" aria-label="Ornate pink crest framing a portrait of a hooded guide"></div>
      <svg class="close" viewBox="0 0 28 28" aria-label="Close"><path d="M3 3L25 25M25 3L3 25" stroke="var(--close)" stroke-width="3.5"/></svg>
      <div class="copy">
        <p class="quote">'If your actions inspire others to dream more, learn more, do more and become more, you are a leader'</p>
        <p>A leader must have a mission and a clear vision in their mind to inspire their team. They must know their team well, they must understand them. They then need to set out a series of small steps in order to guide their team toward achieving their mission.</p>
        <p>At the same time they're doing this they must recognize and show appreciation to everyone and keep communcation strong. Then there's everything else...</p>
      </div>
      <div class="card-rule thick"></div>
      <div class="card-rule thin"></div>
    </div>
    <button class="next-button">NEXT</button>
  </section>

</main>
</body>
</html>
```